Colour consulting and Interior design company needs a squarespace web design

we need a website design for squarespace for a Melbourne based company called 'Brightwell Rooms' which incorporates the existing logo. The company primarily provides colour consulting for residential and commercial as well as interior design services. Schemes are personalised for each client. I would like the design to have some colour and use the colour palette provided but it is not is not totally exclusive. The final design should indicate character, playfulness, functionality , harmony and joy. I like the blue/green core colour with the white and would like that to be incorporated.
as per image provided below - double sided
4 page
- space for some images but not too many.
- Page for booking consultation
- real images of houses

```html
<!DOCTYPE html>
<html lang="en">
<head>
<meta charset="utf-8">
<title>Brightwell Rooms</title>
<link rel="stylesheet" href="https://fonts.googleapis.com/css2?family=Montserrat:wght@500;600;700;800&family=Open+Sans:wght@400;600&display=swap">
<style>
:root{
  --teal:#155d78;
  --teal-dark:#0f4d66;
  --nav-active:#1d8cc2;
  --ink:#111;
  --body:#333;
  --white:#fff;
  --muted:#f4f4f4;
}
*{box-sizing:border-box;margin:0;padding:0}
html,body{width:1200px;height:4627px;overflow:hidden;background:var(--white)}
body{position:relative;font-family:"Open Sans",sans-serif;color:var(--body)}
.abs{position:absolute}
.btn{position:absolute;display:flex;align-items:center;justify-content:center;background:var(--teal);color:var(--white);font:700 14px "Montserrat",sans-serif;text-transform:uppercase;letter-spacing:.3px}
.photo{position:absolute}
/* header */
.site-header{position:absolute;left:0;top:0;width:1200px;height:103px;background:var(--white)}
.brand{position:absolute;left:140px;top:28px;display:flex;align-items:center;gap:14px;font:700 32px "Montserrat",sans-serif;color:var(--teal)}
.brand-mark{width:34px;height:34px;border-radius:50%;background:var(--teal)}
.main-nav{position:absolute;left:532px;top:41px;display:flex;gap:10px}
.main-nav a{font:600 14px "Montserrat",sans-serif;color:var(--ink);text-decoration:none;padding:6px 12px;text-transform:uppercase}
.main-nav a.active{background:var(--nav-active);color:var(--white)}
/* hero */
.hero{left:0;top:103px;width:1200px;height:600px;background:linear-gradient(135deg,#cfe3a0 0%,#e9ecc6 40%,#9fd18a 70%,#b98a55 100%)}
.hero-title{position:absolute;left:0;top:480px;width:1200px;text-align:center;font:800 40px/44px "Montserrat",sans-serif;color:var(--white);text-transform:uppercase;text-shadow:0 2px 6px rgba(0,0,0,.35)}
/* services */
.section-title{position:absolute;left:0;width:1200px;text-align:center;font:700 30px "Montserrat",sans-serif;color:var(--ink);text-transform:uppercase}
.rule{position:absolute;left:582px;width:36px;height:2px;background:var(--ink)}
.card{position:absolute;top:858px;width:368px;height:459px;background:var(--white);box-shadow:0 2px 10px rgba(0,0,0,.15)}
.card .photo{left:0;top:0;width:368px;height:290px}
.card h3{position:absolute;left:34px;top:314px;font:700 17px "Montserrat",sans-serif;color:var(--ink);text-transform:uppercase}
.card p{position:absolute;left:34px;top:340px;width:300px;font-size:14px;line-height:18px;color:var(--ink)}
.card .btn{left:34px;top:400px;width:96px;height:32px;font-size:12px}
/* bands */
.band-title{position:absolute;font:800 34px/40px "Montserrat",sans-serif;color:var(--ink);text-transform:uppercase}
.band-text{position:absolute;font-size:15px;line-height:19px;color:var(--ink)}
.split-title{position:absolute;left:144px;font:800 34px/41px "Montserrat",sans-serif;color:var(--ink);text-transform:uppercase}
.split-text{position:absolute;left:144px;width:380px;font-size:14px;line-height:19px;color:var(--body)}
/* footer */
.site-footer{position:absolute;left:0;top:4242px;width:1200px;height:385px;background:var(--teal)}
.footer-topline{position:absolute;left:0;top:0;width:1200px;height:6px;background:var(--teal-dark)}
.footer-nav{position:absolute;left:0;top:54px;width:1200px;display:flex;justify-content:center;gap:10px;font:600 13px "Montserrat",sans-serif;color:var(--white);text-transform:uppercase}
.footer-brand{position:absolute;left:0;top:125px;width:1200px;display:flex;justify-content:center;align-items:center;gap:14px;font:700 36px "Montserrat",sans-serif;color:var(--white)}
.footer-brand .brand-mark{background:var(--white);width:40px;height:40px}
.footer-address{position:absolute;left:0;top:248px;width:1200px;text-align:center;font-size:12px;color:var(--white)}
.copyright{position:absolute;left:0;top:335px;width:1200px;text-align:center;font-size:12px;color:var(--white)}
</style>
</head>
<body>

<header class="site-header">
  <div class="brand"><span class="brand-mark"></span>Brightwell Rooms</div>
  <nav class="main-nav">
    <a class="active">Home</a><a>About Us</a><a>Services</a><a>Gallery</a><a>Blog</a><a>Contact Us</a>
  </nav>
</header>

<section>
  <div class="photo hero" role="img" aria-label="Bright living room with lime green walls, green sofa, wooden floor and dining table"></div>
  <h1 class="hero-title abs">Colour Consulting<br>For Residential</h1>
  <a class="btn" style="left:442px;top:595px;width:316px;height:60px;font-size:22px">Book Consultation</a>
</section>

<section>
  <h2 class="section-title" style="top:752px">Our Services</h2>
  <div class="rule" style="top:806px"></div>

  <article class="card" style="left:25px">
    <div class="photo" role="img" aria-label="Modern two storey residential house with garden" style="background:linear-gradient(180deg,#9cc6e8 0%,#dfe8ee 45%,#6f7b6a 70%,#3f7a3a 100%)"></div>
    <h3>Residential</h3>
    <p>Lorem Ipsum is simply dummy text of the printing and typesetting industry</p>
    <a class="btn">Read More</a>
  </article>
  <article class="card" style="left:416px">
    <div class="photo" role="img" aria-label="Glass office towers seen from below against a blue sky" style="background:linear-gradient(160deg,#2f5f9a 0%,#8fb6dc 45%,#d9c39b 75%,#4c5a6e 100%)"></div>
    <h3>Commercial</h3>
    <p>Lorem Ipsum is simply dummy text of the printing and typesetting industry</p>
    <a class="btn">Read More</a>
  </article>
  <article class="card" style="left:810px">
    <div class="photo" role="img" aria-label="Light interior lounge with curtains and white sofa" style="background:linear-gradient(180deg,#ece7df 0%,#d8c6a4 50%,#f2efe9 100%)"></div>
    <h3>Interior Design</h3>
    <p>Lorem Ipsum is simply dummy text of the printing and typesetting industry</p>
    <a class="btn">Read More</a>
  </article>
</section>

<section>
  <div class="photo" role="img" aria-label="Bedroom with half orange painted wall, grey bed and framed picture" style="left:0;top:1385px;width:1200px;height:546px;background:linear-gradient(90deg,#b2541a 0%,#d9782c 35%,#c9c9c6 55%,#eeeeec 100%)"></div>
  <h2 class="band-title" style="left:640px;top:1478px;width:364px;text-align:right">Colour<br>Consultation</h2>
  <p class="band-text" style="left:680px;top:1570px;width:324px;text-align:right">Lorem Ipsum is simply dummy text of the printing and typesetting industry ontent of a page when looking at its layout. The point of using.</p>
  <a class="btn" style="left:864px;top:1665px;width:140px;height:40px">Read More</a>
</section>

<section>
  <h2 class="split-title" style="top:2072px">Design Advice</h2>
  <p class="split-text" style="top:2145px">Lorem ipsum dolor sit amet, consectetur adipiscing elit, sed do eiusmod tempor incididunt ut labore et dolore magna aliqua. Ut enim ad minim veniam, quis nostrud exercitation ullamco laboris nisi ut aliquip ex ea commodo consequat. Duis aute irure dolor in reprehenderit in voluptate velit esse cillum dolore eu fugiat nulla pariatur. Excepteur sint occaecat cupidatat non proident, sunt in culpa qui officia deserunt mollit.</p>
  <a class="btn" style="left:144px;top:2329px;width:136px;height:38px">Read More</a>
  <div class="photo" role="img" aria-label="Modern house with wooden panels and white balcony against a blue sky" style="left:574px;top:1987px;width:571px;height:459px;background:linear-gradient(180deg,#2d76c9 0%,#8ab8e6 40%,#a0623a 60%,#d9d6cf 85%,#8b8b86 100%)"></div>
</section>

<section>
  <div class="photo" role="img" aria-label="Grey blue living room with white sofa, shelves and window onto palm trees" style="left:0;top:2508px;width:1200px;height:546px;background:linear-gradient(90deg,#b9c7b4 0%,#7f9a6b 25%,#8a95ae 50%,#7b86a4 100%)"></div>
  <h2 class="band-title" style="left:600px;top:2600px;width:460px;text-align:center;color:var(--white)">Experience</h2>
  <p class="band-text" style="left:600px;top:2660px;width:460px;text-align:center;color:var(--white)">Lorem Ipsum is simply dummy text of the printing and typesetting industry ontent of a page when looking at its layout. The point of using.</p>
  <a class="btn" style="left:788px;top:2736px;width:136px;height:38px">Read More</a>
</section>

<section>
  <h2 class="split-title" style="top:3167px">Residential &amp;<br>Commercial Colour<br>Design Specialists</h2>
  <p class="split-text" style="top:3303px">Lorem ipsum dolor sit amet, consectetur adipiscing elit, sed do eiusmod tempor incididunt ut labore et dolore magna aliqua. Ut enim ad minim veniam, quis nostrud exercitation ullamco laboris nisi ut aliquip ex ea commodo consequat. Duis aute irure dolor in reprehenderit in voluptate velit esse cillum dolore eu fugiat nulla pariatur. Excepteur sint occaecat cupidatat non proident, sunt in culpa qui officia deserunt mollit.</p>
  <a class="btn" style="left:144px;top:3486px;width:136px;height:38px">Read More</a>
  <div class="photo" role="img" aria-label="White lounge with lime green feature wall and black sofa" style="left:574px;top:3110px;width:571px;height:459px;background:linear-gradient(90deg,#d7d7d3 0%,#eaeae6 35%,#8cc63f 55%,#e8e8e4 75%,#cfcfca 100%)"></div>
</section>

<section>
  <div class="photo" role="img" aria-label="White bedroom with grey bed, pendant lamps, flowers and paint drop artwork" style="left:0;top:3634px;width:1200px;height:608px;background:linear-gradient(180deg,#f3f3f1 0%,#e6e5e2 60%,#a8a7b8 85%,#d9d3c7 100%)"></div>
  <h2 class="band-title" style="left:0;top:3688px;width:1200px;text-align:center;color:#333;font-size:32px;line-height:38px">We Invite You To<br>Create, Your Way!</h2>
  <p class="band-text" style="left:420px;top:3774px;width:360px;text-align:center;color:var(--teal)">Lorem Ipsum is simply dummy text of the printing and typesetting industry ontent of a page when.</p>
  <a class="btn" style="left:538px;top:3952px;width:136px;height:38px">Read More</a>
</section>

<footer class="site-footer">
  <div class="footer-topline"></div>
  <nav class="footer-nav"><span>Home</span><span>|</span><span>About Us</span><span>|</span><span>Services</span><span>|</span><span>Gallery</span><span>|</span><span>Blog</span><span>|</span><span>Contact Us</span></nav>
  <div class="footer-brand"><span class="brand-mark"></span>Brightwell Rooms</div>
  <p class="footer-address">48 Larkspur Lane &nbsp;|&nbsp; Fernvale, VIC 3094 &nbsp;|&nbsp; T: 03 5550 0147</p>
  <p class="copyright">Copyrights @ 2018 All Rights Reserved</p>
</footer>

</body>
</html>
```